Kessel Fahrwerkstatt
Sehr angenehme zusammenarbeit nicht aufdringlich und genau auf die Wünsche eingegangen. Wir werde sicher noch mehr zusammen Arbeiten. Gruss Lukas Hemmerle Inhaber Kessel Fahrwerkstatt
Zielgruppe
Dinks und Kunden mit viel Erfolg und hohem Ausgabepotential.
Aufgabenstellung
Unsere Firma vertreibt Fahrzeuge im Luxusbereich hauptgebiet Valtro aber auch andere Sportwagen. Was uns fehlt ist ein optischer Wiedererkennugswert. Deshalb hätten wir gerne ein Visitenkarten Design und Briefpapier Design. Später soll auch noch eine Webseite mit gleichem Wiedererkennungswert entstehen. " Roter Faden "

```html
<!DOCTYPE html>
<html lang="de">
<head>
<meta charset="utf-8">
<title>Kessel Fahrwerkstatt – Visitenkarte</title>
<link rel="stylesheet" href="https://fonts.googleapis.com/css2?family=Source+Sans+3:wght@300;400&display=swap">
<style>
  :root {
    --backdrop: #e8e4de;
    --navy-light: #23336b;
    --navy-dark: #0d1842;
    --paper: #ffffff;
    --gold: #c9a25e;
    --gold-light: #e9cf95;
    --gold-dark: #9a7336;
    --contact-text: #9ea7c7;
  }
  * { margin: 0; padding: 0; box-sizing: border-box; }
  html, body { width: 1200px; height: 800px; overflow: hidden; }
  body {
    background: var(--backdrop);
    font-family: "Source Sans 3", sans-serif;
    position: relative;
  }
  .card {
    position: absolute;
    width: 500px;
    height: 300px;
  }
  .card--front { left: 90px; top: 230px; }
  .card--back { left: 610px; top: 250px; }
  .card__shape {
    position: absolute;
    inset: 0;
    width: 500px;
    height: 300px;
  }
  .brand {
    position: absolute;
    display: flex;
    align-items: center;
    gap: 16px;
  }
  .brand__dot {
    width: 38px;
    height: 38px;
    border-radius: 50%;
    background: var(--gold);
    flex: none;
  }
  .brand__name {
    color: var(--gold);
    font-weight: 300;
    text-transform: uppercase;
    line-height: 1.05;
  }
  .brand__line1 { display: block; font-size: 34px; letter-spacing: 1px; }
  .brand__line2 { display: block; font-size: 17px; letter-spacing: 6px; }
  .card--front .brand { left: 48px; top: 118px; }
  .card--back .brand { left: 120px; top: 138px; }
  .contact {
    position: absolute;
    left: 36px;
    bottom: 28px;
    color: var(--contact-text);
    font-size: 11.5px;
    font-weight: 300;
    line-height: 1.55;
    list-style: none;
  }
</style>
</head>
<body>

<svg width="0" height="0" style="position:absolute" aria-hidden="true">
  <defs>
    <linearGradient id="navyFill" x1="0" y1="0" x2="1" y2="1">
      <stop offset="0" stop-color="#1a2858"/>
      <stop offset="0.45" stop-color="#23336b"/>
      <stop offset="1" stop-color="#0d1842"/>
    </linearGradient>
    <linearGradient id="goldEdge" x1="0" y1="0" x2="1" y2="0">
      <stop offset="0" stop-color="#9a7336"/>
      <stop offset="0.3" stop-color="#e9cf95"/>
      <stop offset="0.6" stop-color="#c9a25e"/>
      <stop offset="0.85" stop-color="#f1dcaa"/>
      <stop offset="1" stop-color="#9a7336"/>
    </linearGradient>
  </defs>
</svg>

<article class="card card--front" aria-label="Visitenkarte Vorderseite">
  <svg class="card__shape" viewBox="0 0 500 300" aria-hidden="true">
    <path d="M0,48 C70,22 150,8 220,14 C270,18 300,40 345,34 C390,28 420,10 455,16 L500,72 L500,300 L0,300 Z" fill="url(#navyFill)"/>
    <path d="M0,48 C70,22 150,8 220,14 C270,18 300,40 345,34 C390,28 420,10 455,16 L500,72" fill="none" stroke="url(#goldEdge)" stroke-width="5"/>
  </svg>
  <div class="brand">
    <span class="brand__dot"></span>
    <span class="brand__name">
      <span class="brand__line1">Kessel</span>
      <span class="brand__line2">Fahrwerkstatt</span>
    </span>
  </div>
  <ul class="contact">
    <li>Marion Kettler | Geschäftsführerin | Tel.: +49 (0)30 5550182</li>
    <li>Lindenweg 27 | 43120 Hofstetten | Fax: +49 (0)30 5550183</li>
    <li>Mobil: +49 (0)170 5550184 | E-Mail: info@kessel-fahrwerk.de</li>
  </ul>
</article>

<article class="card card--back" aria-label="Visitenkarte Rückseite">
  <svg class="card__shape" viewBox="0 0 500 300" aria-hidden="true">
    <path d="M0,34 C50,14 120,4 180,8 C230,12 250,26 290,20 C340,12 380,2 420,10 C450,18 470,40 490,62 L500,74 L500,300 L0,300 Z" fill="var(--paper)"/>
    <path d="M0,34 C50,14 120,4 180,8 C230,12 250,26 290,20 C340,12 380,2 420,10 C450,18 470,40 490,62 L500,74" fill="none" stroke="url(#goldEdge)" stroke-width="5"/>
  </svg>
  <div class="brand">
    <span class="brand__dot"></span>
    <span class="brand__name">
      <span class="brand__line1">Kessel</span>
      <span class="brand__line2">Fahrwerkstatt</span>
    </span>
  </div>
</article>

</body>
</html>
```